Brava Set CEO and Partners Business Card

We need a fresh, fun, simple and clean business card design....we would like a template where we can add a name and title (as well as specific email addresses). We are open to different looks (full logo on one side and a small logo on the company info side, or our logo is in the background but faint on one side but full on the other, or something else cool :-) ). Our colors are in our logo: blue, black and white...however we are not opposed to the use of other colors if it works. We build sets, make props and a host of other things for the film and television industry...our card should reflect creativity, style and professionalism.

A white background would be preferred.

I would like to see an option with Facebook and Instagram icons.

Facebook- facebook.com/bravasetny
Instagram- brava_set

Our website is bravaset-example.com.

Brava Set, Inc.
418 Corvell Avenue, Unit 9
North Hollywood, California 91602
555.210.4873 | tel
555.210.6692 | fax
www.BravaSet-example.com

Sample Name and Title #1:

Peter Halvik
CEO / Co-Owner
555.210.4873 | tel
555.210.6692 | fax
peter@bravaset-example.com
www.BravaSet-example.com

Target Market(s)

Marketing Professionals, Production Designers, Interior Designers, Film Producers, Directors, Art Directors, Event Directors

Industry/Entity Type

Entertainment Industry

Contact Information for Business Card

Peter Halvik
CEO / Co-Owner
555.210.4873 | tel
555.210.6692 | fax
peter@bravaset-example.com
www.BravaSet-example.com

Font styles to use
Sans Serif

Colors
33a6d7
ffffff
1b1b1b

Requirements
Must have
• Logo, All Contact Info, White Background. Symmetry.
Nice to have
• Facebook and Instagram icons with addresses
• Facebook- facebook.com/bravasetny
• Instagram- brava_set

```html
<!DOCTYPE html>
<html lang="en">
<head>
<meta charset="utf-8">
<title>Brava Set — Business Card</title>
<link href="https://fonts.googleapis.com/css2?family=Open+Sans:wght@400;600;700;800&display=swap" rel="stylesheet">
<style>
  :root {
    --brand-blue: #33a6d7;
    --brand-black: #1b1b1b;
    --card-white: #ffffff;
    --band-dark: #2b2c2e;
    --text-grey: #555a5e;
    --stage: #1f1f21;
  }
  * { box-sizing: border-box; margin: 0; padding: 0; }
  html, body {
    width: 1200px; height: 1000px; overflow: hidden;
    background: var(--stage);
    font-family: "Open Sans", Arial, sans-serif;
  }
  .sheet {
    position: relative; width: 1200px; height: 1000px;
    display: flex; flex-direction: column; align-items: center;
    justify-content: center; gap: 40px;
  }
  .card {
    position: relative; width: 720px; height: 410px;
    background: var(--card-white); border-radius: 28px; overflow: hidden;
    box-shadow: 0 14px 30px rgba(0,0,0,.45);
  }
  .wordmark {
    display: flex; align-items: center; gap: 14px;
    font-weight: 800; color: var(--brand-black); letter-spacing: -1px;
    text-transform: uppercase; white-space: nowrap;
  }
  .wordmark-dot { border-radius: 50%; background: var(--brand-blue); flex: none; }
  .card-front .wordmark {
    position: absolute; left: 50%; top: 50%; transform: translate(-50%, -50%);
    font-size: 78px;
  }
  .card-front .wordmark-dot { width: 30px; height: 30px; }

  .card-back .wordmark {
    position: absolute; left: 50px; top: 150px; font-size: 42px; gap: 10px;
  }
  .card-back .wordmark-dot { width: 16px; height: 16px; }

  .band { position: absolute; inset: 0; width: 100%; height: 100%; }

  .person { position: absolute; right: 48px; top: 44px; text-align: right; }
  .person-name {
    font-size: 30px; font-weight: 700; color: var(--brand-black);
    letter-spacing: .5px; text-transform: uppercase; line-height: 1.1;
  }
  .person-name .surname { color: var(--brand-blue); }
  .person-title { font-size: 17px; font-weight: 600; color: var(--brand-black); margin-top: 2px; }
  .address {
    position: absolute; right: 48px; top: 120px; text-align: right;
    font-size: 15px; color: var(--text-grey); line-height: 1.35;
  }

  .social {
    position: absolute; right: 40px; top: 226px;
    display: flex; gap: 22px; color: #d9dadb; font-size: 15px;
  }
  .social-item { display: flex; align-items: center; gap: 7px; }
  .social-dot { width: 18px; height: 18px; border-radius: 50%; background: var(--brand-blue); }

  .contact-list {
    position: absolute; left: 52px; top: 296px; list-style: none;
    color: var(--card-white); font-size: 18px; line-height: 24px;
  }
  .contact-list li { display: flex; align-items: center; gap: 14px; }
  .contact-list svg { width: 16px; height: 16px; fill: var(--brand-blue); flex: none; }
  .contact-list .accent { color: var(--brand-blue); }
</style>
</head>
<body>
<main class="sheet">

  <section class="card card-front" aria-label="Card front">
    <div class="wordmark"><span class="wordmark-dot"></span>Brava Set</div>
  </section>

  <section class="card card-back" aria-label="Card back">
    <svg class="band" viewBox="0 0 720 410" preserveAspectRatio="none" aria-hidden="true">
      <path d="M0,262 Q300,168 720,168 L720,410 L0,410 Z" fill="var(--brand-blue)"/>
      <path d="M0,279 Q300,185 720,184 L720,410 L0,410 Z" fill="var(--band-dark)"/>
    </svg>

    <div class="wordmark"><span class="wordmark-dot"></span>Brava Set</div>

    <div class="person">
      <p class="person-name">Peter <span class="surname">Halvik</span></p>
      <p class="person-title">CEO/Co-Owner</p>
    </div>

    <address class="address" style="font-style:normal">
      418 Corvell Avenue, Unit 9<br>
      North Hollywood, California 91602
    </address>

    <div class="social">
      <span class="social-item"><span class="social-dot"></span>/bravasetny</span>
      <span class="social-item"><span class="social-dot"></span>/brava_set</span>
    </div>

    <ul class="contact-list">
      <li>
        <svg viewBox="0 0 16 16" aria-hidden="true"><path d="M3.5 1.5l2.5 0 1.2 3-1.7 1.2c.8 1.8 2 3 3.8 3.8l1.2-1.7 3 1.2v2.5c0 .8-.7 1.5-1.5 1.5C6.6 13 3 9.4 2 4 2 2.2 2.7 1.5 3.5 1.5z"/></svg>
        555 210 4873
      </li>
      <li>
        <svg viewBox="0 0 16 16" aria-hidden="true"><rect x="4" y="1.5" width="8" height="4"/><rect x="1.5" y="6" width="13" height="6" rx="1"/><rect x="4" y="10" width="8" height="4.5"/></svg>
        555 210 6692
      </li>
      <li>
        <svg viewBox="0 0 16 16" aria-hidden="true"><path d="M1 3.5h14v9H1z M1.5 4l6.5 5 6.5-5" stroke="var(--band-dark)" stroke-width="1"/></svg>
        peter@bravaset-example.com
      </li>
      <li>
        <svg viewBox="0 0 16 16" aria-hidden="true"><circle cx="8" cy="8" r="7"/><path d="M1 8h14M8 1c-3 3.5-3 10.5 0 14M8 1c3 3.5 3 10.5 0 14" stroke="var(--band-dark)" stroke-width="1" fill="none"/></svg>
        <span>www.<span class="accent">bravaset-example</span>.com</span>
      </li>
    </ul>
  </section>

</main>
</body>
</html>
```